van wrap for house/commercial painting company

We are rebranding and i need a new design for a los angeles based painting company.  New business name will be Halden Painting and the vehicle is a toba kestrel 2300.
We offer our services to houses, hoa's, commercial and specializing in interior/exterior, wood staining, cabinet refinishing, drywall repair.
We would love a colorful but easy to read design to grab attention when at job sites or on the road.
I attached our current wrap which we no longer like and looking for a different look/feel. I attached our current logo but the color splash is not necessary if  design flows better without it.

Industry/Entity Type
house painting
Requirements
Must have
- easy to read phone number and contact info

```html
<!DOCTYPE html>
<html lang="en">
<head>
<meta charset="utf-8">
<title>Halden Painting — Van Wrap Layout</title>
<link href="https://fonts.googleapis.com/css2?family=Montserrat:wght@500;800&family=Oswald:wght@400;500&family=Roboto:wght@500&display=swap" rel="stylesheet">
<style>
  :root{
    --stage:#5f5f5f;
    --wrap-white:#f4f4f4;
    --ink:#1f1f22;
    --trim:#2a2a2c;
    --purple:#7a3a9a;
    --orange:#e2692c;
    --splash-red:#e0263a;
    --splash-orange:#f07a1e;
    --splash-yellow:#f6c52b;
    --splash-purple:#7b2c86;
  }
  *{box-sizing:border-box;margin:0;padding:0}
  html,body{width:1200px;height:779px;overflow:hidden;background:var(--stage)}
  .canvas{position:relative;width:1200px;height:779px}
  .wrap-panel{position:absolute;background:var(--wrap-white);border-radius:10px;overflow:hidden}
  .panel-band{position:absolute;left:0;right:0;background:var(--trim)}
  .door-seam{position:absolute;top:0;width:2px;background:#cfcfcf}
  .logo-mark{position:absolute;border-radius:50%;
    background:radial-gradient(circle at 45% 45%,var(--splash-red) 0%,var(--splash-orange) 45%,var(--splash-yellow) 62%,var(--splash-purple) 75%,transparent 76%)}
  .brand-name{position:absolute;font-family:'Montserrat',sans-serif;font-weight:800;color:var(--ink);line-height:1;letter-spacing:1px}
  .brand-sub{position:absolute;font-family:'Montserrat',sans-serif;font-weight:500;color:var(--ink);line-height:1}
  .phone{position:absolute;font-family:'Roboto',sans-serif;font-weight:500;color:var(--purple);line-height:1;white-space:nowrap}
  .website{position:absolute;font-family:'Oswald',sans-serif;color:var(--purple);line-height:1;letter-spacing:.5px;white-space:nowrap}
  .licensed{position:absolute;font-family:'Oswald',sans-serif;color:var(--ink);text-align:center;line-height:1.15}
  .services{position:absolute;display:flex;flex-wrap:wrap;gap:4px 6px}
  .service-pill{font-family:'Oswald',sans-serif;color:#fff;background:var(--orange);border-radius:6px;padding:1px 6px;line-height:1.3;white-space:nowrap}
  .socials{position:absolute;display:flex;align-items:center;gap:5px;font-family:'Oswald',sans-serif;color:var(--ink);white-space:nowrap}
  .social-name{font-weight:500}
  .social-dot{width:7px;height:7px;background:var(--splash-red);display:inline-block}
  .license{font-size:4px;line-height:1.2}
</style>
</head>
<body>
<main class="canvas">

  <!-- Driver side -->
  <section class="wrap-panel side-driver" style="left:75px;top:112px;width:555px;height:210px">
    <div class="panel-band" style="top:178px;height:32px"></div>
    <div class="logo-mark" role="img" aria-label="Colourful paint splash logo mark" style="left:150px;top:6px;width:125px;height:112px"></div>
    <div class="brand-name" style="left:362px;top:30px;font-size:34px">HALDEN</div>
    <div class="brand-sub" style="left:384px;top:72px;font-size:15px;letter-spacing:6px">PAINTING</div>
    <div class="phone" style="left:372px;top:94px;font-size:22px">213-555-0148</div>
    <div class="website" style="left:88px;top:116px;font-size:11px">www.haldenpainting.com</div>
    <div class="licensed" style="left:160px;top:134px;font-size:10px">Fully Licensed,<br>Bonded &amp;<br>Insured</div>
    <div class="services" style="left:240px;top:125px;width:170px;font-size:7px">
      <span class="service-pill">EXTERIOR &amp; INTERIOR</span>
      <span class="service-pill">COMMERCIAL &amp; RESIDENTIAL</span>
      <span class="service-pill">CABINET REFINISHING</span>
      <span class="service-pill">GARAGE FLOORS</span>
      <span class="service-pill">DRYWALL REPAIR &amp; MORE!</span>
    </div>
    <div class="socials" style="left:432px;top:124px;font-size:9px">
      <span class="social-name">Ratewell</span><span class="social-dot"></span>
      <span class="license">JOHN 1:12-13<br>LICENSE #4471203</span>
    </div>
  </section>

  <!-- Front hood -->
  <section class="wrap-panel front-hood" style="left:820px;top:190px;width:270px;height:90px">
    <div class="panel-band" style="top:70px;height:20px"></div>
    <div class="logo-mark" role="img" aria-label="Colourful paint splash logo mark" style="left:60px;top:12px;width:42px;height:40px"></div>
    <div class="brand-name" style="left:108px;top:18px;font-size:16px">HALDEN</div>
    <div class="brand-sub" style="left:116px;top:37px;font-size:6px;letter-spacing:3px">PAINTING</div>
  </section>

  <!-- Passenger side -->
  <section class="wrap-panel side-passenger" style="left:75px;top:430px;width:570px;height:215px">
    <div class="panel-band" style="top:180px;height:35px"></div>
    <div class="brand-name" style="left:25px;top:33px;font-size:34px">HALDEN</div>
    <div class="brand-sub" style="left:47px;top:76px;font-size:15px;letter-spacing:6px">PAINTING</div>
    <div class="phone" style="left:25px;top:103px;font-size:22px">213-555-0148</div>
    <div class="socials" style="left:30px;top:130px;font-size:9px">
      <span class="social-name">Ratewell</span><span class="social-dot"></span>
      <span class="license">JOHN 1:12-13<br>LICENSE #4471203</span>
    </div>
    <div class="logo-mark" role="img" aria-label="Colourful paint splash logo mark" style="left:195px;top:6px;width:130px;height:115px"></div>
    <div class="services" style="left:150px;top:128px;width:180px;font-size:7.5px;justify-content:flex-end">
      <span class="service-pill">EXTERIOR &amp; INTERIOR</span>
      <span class="service-pill">COMMERCIAL &amp; RESIDENTIAL</span>
      <span class="service-pill">CABINET REFINISHING</span>
      <span class="service-pill">GARAGE FLOORS</span>
      <span class="service-pill">DRYWALL REPAIR &amp; MORE!</span>
    </div>
    <div class="website" style="left:355px;top:112px;font-size:11px">www.haldenpainting.com</div>
    <div class="licensed" style="left:372px;top:136px;font-size:10px">Fully Licensed,<br>Bonded &amp;<br>Insured</div>
  </section>

  <!-- Rear doors -->
  <section class="wrap-panel rear-doors" style="left:805px;top:432px;width:220px;height:200px">
    <div class="panel-band" style="top:174px;height:26px"></div>
    <div class="door-seam" style="left:109px;height:200px"></div>
    <div class="logo-mark" role="img" aria-label="Colourful paint splash logo mark" style="left:16px;top:12px;width:86px;height:76px"></div>
    <div class="brand-name" style="left:118px;top:36px;font-size:17px">HALDEN</div>
    <div class="brand-sub" style="left:124px;top:56px;font-size:7px;letter-spacing:3px">PAINTING</div>
    <div class="website" style="left:119px;top:76px;font-size:6.5px">www.haldenpainting.com</div>
    <div class="phone" style="left:14px;top:101px;font-size:13px">213-555-0148</div>
    <div class="socials" style="left:143px;top:105px;font-size:6px">
      <span class="social-name">Ratewell</span><span class="social-dot" style="width:5px;height:5px"></span>
    </div>
    <div class="services" style="left:118px;top:118px;width:70px;font-size:4.5px;flex-direction:column;align-items:flex-start;gap:2px">
      <span class="service-pill">EXTERIOR &amp; INTERIOR</span>
      <span class="service-pill">COMMERCIAL &amp; RESIDENTIAL</span>
      <span class="service-pill">CABINET REFINISHING</span>
      <span class="service-pill">GARAGE FLOORS</span>
      <span class="service-pill">DRYWALL REPAIR &amp; MORE!</span>
    </div>
  </section>

</main>
</body>
</html>
```